Private Investment Partnership needs Business Card Design

We are a brand-new private investment partnership looking for business card design help. It will be called The Corvale + Vantry Partnership. We are based in NYC (hence Corvale) and our other partner is a firm called Vantry Resources which has roots in Pittsburgh, PA. We are looking for something a bit more formal and professional- probably typographic oriented in a font like Adobe Garamond. We might want to incorporate the colors PMS Yellow 1235 and PMS Blue 282. Attached is a pretty plain, old example of something.

```html
<!DOCTYPE html>
<html lang="en">
<head>
<meta charset="utf-8">
<title>The Corvale + Vantry Partnership – Business Card</title>
<link rel="stylesheet" href="https://fonts.googleapis.com/css2?family=EB+Garamond:wght@400;500;600;700&display=swap">
<style>
  :root {
    --page-bg: #e4e4e6;
    --card-white: #ffffff;
    --brand-blue: #474d75;
    --brand-blue-light: #5a618a;
    --brand-yellow: #f2b826;
    --text-light: #e9eaf1;
    --text-soft: #d3d5e2;
  }
  * { margin: 0; padding: 0; box-sizing: border-box; }
  html, body {
    width: 1200px;
    height: 900px;
    overflow: hidden;
    background: var(--page-bg);
    font-family: "EB Garamond", Garamond, serif;
  }
  .card {
    position: absolute;
    left: 100px;
    top: 164px;
    width: 1000px;
    height: 571px;
    background: radial-gradient(ellipse at 45% 55%, var(--brand-blue-light), var(--brand-blue) 70%);
    box-shadow: 0 10px 30px rgba(0,0,0,0.18);
    overflow: hidden;
  }
  .card-header {
    position: absolute;
    left: 0; top: 0;
    width: 100%;
    height: 178px;
    background: var(--card-white);
    border-bottom: 8px solid var(--brand-yellow);
  }
  .brand-square {
    position: absolute;
    left: 58px;
    top: 42px;
    width: 92px;
    height: 92px;
    border: 5px solid var(--brand-yellow);
  }
  .company-name {
    position: absolute;
    left: 176px;
    top: 50px;
    color: var(--brand-blue);
    font-weight: 600;
    font-size: 31px;
    line-height: 1.15;
    letter-spacing: 0.5px;
    text-transform: uppercase;
  }
  .person {
    position: absolute;
    left: 60px;
    top: 330px;
  }
  .person-name {
    color: var(--text-light);
    font-weight: 700;
    font-size: 40px;
    line-height: 1.1;
  }
  .person-title {
    color: var(--text-soft);
    font-size: 30px;
    margin-top: 4px;
  }
  .divider {
    position: absolute;
    left: 470px;
    top: 222px;
    width: 2px;
    height: 262px;
    background: var(--text-soft);
  }
  .contact-list {
    position: absolute;
    left: 540px;
    top: 224px;
    list-style: none;
    color: var(--text-soft);
    font-size: 27px;
  }
  .contact-item {
    display: flex;
    align-items: center;
    height: 44px;
  }
  .contact-icon {
    width: 26px;
    height: 26px;
    margin-right: 24px;
    flex: none;
  }
  .contact-address {
    margin-top: 14px;
    line-height: 1.3;
  }
</style>
</head>
<body>
  <div class="card">
    <header class="card-header">
      <div class="brand-square"></div>
      <div class="company-name">The Corvale<br>Vantry Partnership</div>
    </header>

    <div class="person">
      <div class="person-name">Daniel R. Ashford</div>
      <div class="person-title">Chief Investment Officer</div>
    </div>

    <div class="divider"></div>

    <ul class="contact-list">
      <li class="contact-item">
        <svg class="contact-icon" viewBox="0 0 24 24" aria-hidden="true">
          <path fill="#f2b826" d="M6.6 10.8c1.4 2.8 3.8 5.1 6.6 6.6l2.2-2.2c.3-.3.7-.4 1-.2 1.1.4 2.3.6 3.6.6.6 0 1 .4 1 1V20c0 .6-.4 1-1 1C10.6 21 3 13.4 3 4c0-.6.4-1 1-1h3.5c.6 0 1 .4 1 1 0 1.3.2 2.5.6 3.6.1.3 0 .7-.2 1z"/>
        </svg>
        <span>(203) 555-0148</span>
      </li>
      <li class="contact-item">
        <svg class="contact-icon" viewBox="0 0 24 24" aria-hidden="true">
          <rect x="6" y="1.5" width="12" height="21" rx="2" fill="#f2b826"/>
          <rect x="8" y="4" width="8" height="7" fill="#474d75"/>
          <g fill="#474d75">
            <rect x="8" y="13" width="2" height="2"/><rect x="11" y="13" width="2" height="2"/><rect x="14" y="13" width="2" height="2"/>
            <rect x="8" y="16.5" width="2" height="2"/><rect x="11" y="16.5" width="2" height="2"/><rect x="14" y="16.5" width="2" height="2"/>
          </g>
        </svg>
        <span>(646) 555-0193</span>
      </li>
      <li class="contact-item">
        <svg class="contact-icon" viewBox="0 0 24 24" aria-hidden="true">
          <rect x="1.5" y="5" width="21" height="14" fill="#f2b826"/>
          <path d="M1.5 5 12 13.5 22.5 5" fill="none" stroke="#474d75" stroke-width="1.6"/>
        </svg>
        <span>dashford@corvalevantry.com</span>
      </li>
      <li class="contact-address">
        48 Linden Crest Avenue<br>Marlow Point, CT 06915
      </li>
    </ul>
  </div>
</body>
</html>
```